Business Card and Letterhead for Juniper Anvil - (Have Logo)

Update 4: Removed company reg no from business card details as it looked a bit out of place. Updated services list.
UPDATE 3
Sorry, I got the address a little bit wrong, have updated it below. Sorry for any inconvenience caused.
UPDATE 2
Finally I have the details for the business cards and letterhead. Submissions already made do not have to be updated unless shortlisted, if all new submissions could include the details for me, Marcus, that would be very much appreciated and help with the final shortlist selection. I intend to share a shortlist of the three best entries with past and existing customers for their feedback and opinions. Thank you all again for your time.
Here are the details.
Marcus Telby
Web Developer
T: 01632 960 418
E: marcus@juniperanvil.example
www.juniperanvil.example
Professional Photography
Web Solutions & E-Commerce
Audio & HD Video Production
Marketing & Promotions
Identity and Branding
Juniper Anvil Ltd
Suite 20938, 3rd Floor
212-224 Orchard Lane
London, N7 9QX
Company Reg. No: 05829147
The order and the layout of the information are of course down to the design, but the company registration number should be smaller and less prominent. The formatting of the telephone and email address using a T: and an E: I am not sure about and again if it is Tel: or Email: or Icons is up to the design.
The Company No. on the letterhead should read (somewhere in small text along the bottom):
Juniper Anvil is a Ltd Company registered in England & Wales, Registration No. 05829147.
The second business card details are
Oliver Brackley
Photographer
T: 01632 960 418
E: oliver@juniperanvil.example
Everything else the same of course.
Thank you again for all the submissions so far.
END OF UPDATE 2
-
UPDATE 1: Please do not alter the logo nor the logo colours. (This was a previous pixel forum project and I am extremely happy with it. The icon can stand alone of course, but I have had to eliminate all entries that have made it black and white, or reversed the icon.) I would like to thank everyone that has participated so far and am very grateful for all your thought and time.
End of Update 1
-
Original Brief:
I have attached the logo vector file.
Following a superb logo from a previous Pixel Forum project I am now looking for a business card design and (although less important) a letterhead as well.
I must admit I tried to do it myself but could only come up with the usual amateur stuff that in comparison to the quality of the logo looked awful.
About Us
Juniper Anvil Ltd will be a new company due to start in January. It is really just me (a web developer) and my friend (a photographer). We will be aiming at the usual small to medium sized businesses in the local area, selling various digital services including photographic services to the public, web hosting and development, commercial photography, modelling services (not us!), full video and film production and possibly a bit of marketing as well. (Really it is anything we can do professionally all lumped together! We met running seperate businesses which have both since closed)
We will not be competing on price. We plan to be expensive but fair. Certainly not the cheapest.
What we are looking for
Business Card
I imagine a double sided business card, which will be used for more than one person. I imagine the front to be the same for everyone and the persons details to be on the back, although this is of course only my thoughts and I am of course completely open to any ideas.
The card could also have a services list or a bit about what we do on it. It might feature the website address, our business address (mail forwarding address) or our registered company number.
Or it might have none of that, we are completely open to any ideas and have no real fixed opinions. I just want it to be really nice :-)
Letterhead (secondary importance)
We will make our decision primarily on the business card, although a mathcing letterhead would be fantastic. Something standardish in format and simple, although again, all ideas are welcomed.
I hope that is enough information but if you have any questions I will answer them as fully and as quickly as possible.
Thank you once again and I really look forward to seeing your ideas and picking a winner.
Marcus T.
Small businesses AND the general public
Film Production

```html
<!DOCTYPE html>
<html lang="en">
<head>
<meta charset="utf-8">
<title>Juniper Anvil – Business Cards and Letterhead</title>
<link rel="stylesheet" href="https://fonts.googleapis.com/css2?family=Arimo:wght@400;700&display=swap">
<style>
  :root {
    --brand-red: #c8102e;
    --ink: #1a1a1a;
    --paper: #ffffff;
    --edge: #b5b5b5;
  }
  * { margin: 0; padding: 0; box-sizing: border-box; }
  html, body { width: 1200px; height: 1144px; overflow: hidden; background: var(--paper); }
  body { position: relative; font-family: "Arimo", Arial, sans-serif; color: var(--ink); }

  .card, .letterhead { position: absolute; background: var(--paper); border: 1px solid var(--edge); overflow: hidden; }
  .card { left: 3px; width: 352px; height: 203px; }
  .card--marcus { top: 193px; }
  .card--oliver { top: 398px; }
  .card--services { top: 676px; }

  .wordmark { position: absolute; display: flex; align-items: center; gap: 8px; font-weight: 700; color: var(--ink); white-space: nowrap; }
  .wordmark__square { background: var(--brand-red); flex: none; }
  .card .wordmark { left: 70px; top: 14px; font-size: 26px; }
  .card .wordmark__square { width: 24px; height: 24px; }

  .reg-line { position: absolute; left: 100px; top: 56px; font-size: 7px; }

  .tabs { position: absolute; display: flex; flex-direction: column; }
  .tab { background: var(--brand-red); }
  .card .tabs { left: 0; top: 22px; gap: 12px; }
  .card .tab { width: 28px; height: 9px; }

  .person { position: absolute; left: 44px; top: 82px; font-size: 10px; line-height: 13px; }
  .person__name { font-size: 17px; line-height: 20px; font-weight: 700; color: var(--brand-red); margin-bottom: 4px; white-space: nowrap; }
  .person__role { font-size: 13px; font-weight: 400; color: var(--ink); }
  .person__label { font-weight: 700; color: var(--brand-red); }
  .person__address { margin-top: 4px; }

  .card__band { position: absolute; left: 0; top: 182px; width: 282px; height: 8px; background: var(--ink); }
  .card__mark { position: absolute; left: 276px; top: 96px; width: 58px; height: 58px; background: var(--brand-red); }
  .card__base { position: absolute; left: 280px; top: 172px; width: 60px; height: 28px; background: var(--ink); }

  .card--services .wordmark { left: 70px; top: 16px; }
  .services { position: absolute; left: 10px; top: 80px; list-style: none; font-size: 11px; line-height: 15px; }
  .services li { display: flex; align-items: center; gap: 6px; }
  .services li::before { content: ""; width: 14px; height: 6px; background: var(--brand-red); flex: none; }
  .card--services .web { position: absolute; right: 12px; top: 166px; font-size: 11px; }
  .card--services .card__band { width: 100%; top: 184px; height: 9px; }

  .letterhead { left: 386px; top: 0; width: 812px; height: 1144px; }
  .letterhead .wordmark { right: 26px; top: 28px; font-size: 38px; }
  .letterhead .wordmark__square { width: 36px; height: 36px; }
  .sender { position: absolute; right: 28px; top: 96px; text-align: right; font-size: 12px; line-height: 15px; }
  .letterhead .tabs { right: 0; top: 165px; gap: 16px; }
  .letterhead .tab { width: 30px; height: 14px; }
  .letterhead .web { position: absolute; right: 70px; top: 1060px; font-size: 15px; }
  .letterhead__mark { position: absolute; right: 18px; top: 1040px; width: 34px; height: 36px; background: var(--brand-red); }
  .letterhead__band { position: absolute; left: 0; top: 1082px; width: 100%; height: 10px; background: var(--ink); }
  .legal { position: absolute; left: 0; width: 100%; top: 1112px; text-align: center; font-size: 10px; }
</style>
</head>
<body>

<section class="card card--marcus" aria-label="Business card, Marcus Telby">
  <div class="wordmark"><span class="wordmark__square"></span>Juniper Anvil</div>
  <p class="reg-line">Company Reg. No: 05829147</p>
  <div class="tabs"><span class="tab"></span><span class="tab"></span><span class="tab"></span><span class="tab"></span><span class="tab"></span></div>
  <div class="person">
    <p class="person__name">Marcus Telby <span class="person__role">Web Developer</span></p>
    <p><span class="person__label">Telephone:</span> 01632 960 418</p>
    <p><span class="person__label">Email:</span> marcus@juniperanvil.example</p>
    <p class="person__address">Juniper Anvil Ltd.<br>212-224 Orchard Lane<br>London, N7 9QX</p>
  </div>
  <div class="card__band"></div>
  <div class="card__mark"></div>
  <div class="card__base"></div>
</section>

<section class="card card--oliver" aria-label="Business card, Oliver Brackley">
  <div class="wordmark"><span class="wordmark__square"></span>Juniper Anvil</div>
  <p class="reg-line">Company Reg. No: 05829147</p>
  <div class="tabs"><span class="tab"></span><span class="tab"></span><span class="tab"></span><span class="tab"></span><span class="tab"></span></div>
  <div class="person">
    <p class="person__name">Oliver Brackley <span class="person__role">Photographer</span></p>
    <p><span class="person__label">Telephone:</span> 01632 960 418</p>
    <p><span class="person__label">Email:</span> oliver@juniperanvil.example</p>
    <p class="person__address">Juniper Anvil Ltd.<br>212-224 Orchard Lane<br>London, N7 9QX</p>
  </div>
  <div class="card__band"></div>
  <div class="card__mark"></div>
  <div class="card__base"></div>
</section>

<section class="card card--services" aria-label="Business card, services side">
  <div class="wordmark"><span class="wordmark__square"></span>Juniper Anvil</div>
  <ul class="services">
    <li>Professional Photography</li>
    <li>Web Solutions &amp; E-Commerce</li>
    <li>Audio &amp; HD Video Production</li>
    <li>Marketing &amp; Promotions</li>
    <li>Design, Creation and Inspiration</li>
  </ul>
  <p class="web">www.juniperanvil.example</p>
  <div class="card__band"></div>
</section>

<section class="letterhead" aria-label="Letterhead">
  <div class="wordmark"><span class="wordmark__square"></span>Juniper Anvil</div>
  <p class="sender">Juniper Anvil Ltd.<br>212-224 Orchard Lane<br>London, N7 9QX</p>
  <div class="tabs"><span class="tab"></span><span class="tab"></span><span class="tab"></span><span class="tab"></span><span class="tab"></span></div>
  <p class="web">www.juniperanvil.example</p>
  <div class="letterhead__mark"></div>
  <div class="letterhead__band"></div>
  <p class="legal">Juniper Anvil is a Ltd Company registered in England &amp; Wales, Registration No. 05829147. Company Reg. No: 05829147</p>
</section>

</body>
</html>
```